Fall Postcard Mailers for Roofing Company

We need a postcard for a mailer designed for ShingleGuide. ShingleGuide is professional and personable. Unlike most roofing companies our Advisors are Non-Commissioned so they provide Unbiased advise. Our Advisors provide an In-depth Roof Analysis for each home. This is much like a home inspection report with pictures and description.

Homeowner demographics are upscale neighborhoods with homeowners over 40 years old with properties over $250,000. All pictures and colors can be pulled from www.ShingleGuideMi-example.com and our Facebook page https://www.facebook.com/MyShingleGuide/. We are based in Plymouth, Mi.

I've attached some of our other marketing materials.

Target Market(s)

Homeowners
40 years old and above
Home value over $250,000

Industry/Entity Type

Roofing

Requirements
Must have
• Space designed for mail printing on front
• Add a three discount coupons
• -Up to $2,500 off Roof Replacement
• -FREE Roof Analysis up to $500 value
• -Up to $100 off Roof Repair
• Non-Commissioned Advisors=Unbiased Guidance
• Financing Available
• Company colors:
• G: C-0 M-0 Y-0 K-80
• O: C-0 M-54 Y-95 K-0
Nice to have
• We are trying to drive action: Calls, website visits, inquiries.
• Personable and professional.
Should not have
• Too much open space.

```html
<!DOCTYPE html>
<html lang="en">
<head>
<meta charset="utf-8">
<title>ShingleGuide Fall Postcard Mailer</title>
<link href="https://fonts.googleapis.com/css2?family=Cabin:wght@400;500;700&family=Ubuntu:wght@500;700&family=Roboto+Condensed:wght@400;500&display=swap" rel="stylesheet">
<style>
  :root{
    --orange:#f58a1f;
    --grey:#58595b;
    --grey-dark:#4d4e50;
    --paper:#ffffff;
    --paper-soft:#f3f4f4;
    --backdrop:#2e2e2e;
    --line:#b9babb;
  }
  *{margin:0;padding:0;box-sizing:border-box}
  html,body{width:910px;height:1200px;overflow:hidden;background:var(--backdrop)}
  .postcard{position:absolute;left:118px;width:662px;height:514px;background:var(--paper);overflow:hidden;box-shadow:0 6px 18px rgba(0,0,0,.45)}
  .postcard--front{top:68px}
  .postcard--back{top:642px}
  .shapes{position:absolute;inset:0}
  .abs{position:absolute}
  .brand{position:absolute;left:28px;top:38px;display:flex;align-items:center;gap:10px;font-family:'Cabin',sans-serif;font-weight:500;font-size:44px;color:var(--grey);letter-spacing:-.5px}
  .brand__mark{width:14px;height:14px;background:var(--orange)}
  .headline{font-family:'Ubuntu',sans-serif;font-weight:700;color:#fff;text-align:center;line-height:24px}
  .tagline{font-family:'Ubuntu',sans-serif;font-weight:700;color:var(--orange);font-size:16px;text-align:center}
  .coupon{position:absolute;top:248px;font-family:'Roboto Condensed',sans-serif;color:#fff;text-align:center;line-height:27px}
  .coupon__lead{font-size:16px;line-height:22px}
  .coupon__offer{font-size:21px}
  .coupon-rule{position:absolute;top:242px;height:98px;border-left:1.5px dotted rgba(255,255,255,.7)}
  .body-copy{font-family:'Cabin',sans-serif;color:#fff;text-align:center}
  .callbar{position:absolute;left:23px;top:472px;font-family:'Ubuntu',sans-serif;font-weight:700;font-size:19px;color:#fff;display:flex;align-items:center;gap:30px}
  .callbar__phone{display:flex;align-items:center;gap:8px}
  .site{position:absolute;left:486px;top:476px;font-family:'Cabin',sans-serif;font-weight:700;font-size:16px;color:#fff}
  .badge{position:absolute;width:76px;height:76px;border-radius:50%;background:var(--orange);border:3px solid #fff;box-shadow:0 2px 5px rgba(0,0,0,.35);font-family:'Roboto Condensed',sans-serif;font-weight:500;font-size:14px;color:#fff;display:flex;align-items:center;justify-content:center;text-align:center;line-height:17px}
  .service{position:absolute;top:291px;height:77px;border:2px solid #fff}
  .service__label{position:absolute;top:381px;font-family:'Ubuntu',sans-serif;font-weight:500;font-size:9.5px;color:#fff;text-align:center}
  .return-address{position:absolute;left:380px;top:46px;font-family:'Cabin',sans-serif;font-size:12.5px;line-height:16px;color:var(--grey)}
  .stamp-box{position:absolute;left:554px;top:30px;width:83px;height:64px;border:1.5px solid var(--line)}
  .address-line{position:absolute;left:401px;width:237px;border-top:1.5px solid var(--line)}
</style>
</head>
<body>

<!-- Front of mailer -->
<section class="postcard postcard--front">
  <svg class="shapes" width="662" height="514" viewBox="0 0 662 514">
    <defs>
      <linearGradient id="houseScene" x1="0" y1="0" x2="0.6" y2="1">
        <stop offset="0" stop-color="#8fb6dc"/>
        <stop offset="0.3" stop-color="#9c8a6c"/>
        <stop offset="0.55" stop-color="#c9502a"/>
        <stop offset="0.8" stop-color="#b23a1f"/>
        <stop offset="1" stop-color="#4f8a36"/>
      </linearGradient>
    </defs>
    <polygon points="282,0 662,0 662,444 442,444" fill="url(#houseScene)" role="img" aria-label="Photo of a gabled suburban home behind a red autumn maple tree and black iron fence"/>
    <polygon points="0,114 321,114 362,222 0,222" fill="var(--grey)"/>
    <polygon points="0,224 363,224 418,348 0,348" fill="var(--orange)"/>
    <polygon points="0,348 418,348 446,444 0,444" fill="var(--grey)"/>
    <polygon points="446,468 662,468 662,514 470,514" fill="var(--grey)"/>
    <polygon points="0,458 446,458 470,514 0,514" fill="var(--orange)"/>
  </svg>

  <div class="brand"><span>ShingleGuide</span><span class="brand__mark"></span></div>

  <div class="headline abs" style="left:0;width:330px;top:135px;font-size:18px">PROFESSIONAL ADVICE TAILORED<br>TO YOUR ROOFING NEEDS</div>
  <div class="tagline abs" style="left:0;width:330px;top:184px">Let us meet your roof.</div>

  <div class="coupon" style="left:0;width:146px"><div class="coupon__lead">UP TO</div><div class="coupon__offer">$2,500 off Roof<br>Replacement</div></div>
  <div class="coupon-rule" style="left:145px"></div>
  <div class="coupon" style="left:146px;width:136px"><div class="coupon__lead" style="font-weight:500">FREE</div><div class="coupon__offer">Roof Analysis<br>up to $500 value</div></div>
  <div class="coupon-rule" style="left:282px"></div>
  <div class="coupon" style="left:282px;width:114px"><div class="coupon__lead">UP TO</div><div class="coupon__offer">$100 off<br>Roof Repair</div></div>

  <div class="body-copy abs" style="left:0;width:420px;top:364px;font-size:14.5px;line-height:20px">Our Advisors provide an IN-DEPTH ROOF ANALYSIS<br>for each home.</div>
  <div class="body-copy abs" style="left:0;width:420px;top:410px;font-size:16px;font-weight:700">Non-Commissioned Advisors=Unbiased Guidance</div>

  <div class="badge" style="left:563px;top:378px">FINANCING<br>AVAILABLE</div>

  <div class="callbar"><span>SCHEDULE NOW!</span><span class="callbar__phone"><svg width="20" height="16" viewBox="0 0 20 16" aria-hidden="true"><path d="M1 6 Q10 -1 19 6 L16 8 L14 5 Q10 4 6 5 L4 8 Z" fill="#fff"/><path d="M5 8 L15 8 L18 15 L2 15 Z" fill="#fff"/><circle cx="10" cy="11" r="2" fill="var(--orange)"/></svg>(555) 014-ROOF</span></div>
  <div class="site">shingleguidemi-example.com</div>
</section>

<!-- Back of mailer -->
<section class="postcard postcard--back">
  <svg class="shapes" width="662" height="514" viewBox="0 0 662 514">
    <polygon points="0,0 286,0 442,444 0,444" fill="var(--paper-soft)"/>
    <polygon points="0,182 358,182 442,444 0,444" fill="var(--grey)"/>
    <polygon points="338,182 358,182 358,188" fill="#b8650f"/>
    <polygon points="0,112 338,112 358,182 0,182" fill="var(--orange)"/>
    <polygon points="446,468 662,468 662,514 470,514" fill="var(--grey)"/>
    <polygon points="0,458 446,458 470,514 0,514" fill="var(--orange)"/>
  </svg>

  <div class="brand"><span>ShingleGuide</span><span class="brand__mark"></span></div>

  <div class="headline abs" style="left:0;width:332px;top:128px;font-size:19px">SOUTHEAST MICHIGAN'S LEADING<br>ROOFING SYSTEM EXPERTS</div>

  <div class="body-copy abs" style="left:0;width:346px;top:199px;font-size:15.5px;line-height:19.6px">Providing accurate roof analysis, certified leak detection, repairs, and roof replacements in Plymouth, Westland, Livonia, and surrounding cities in Metro Detroit.</div>

  <div class="service" style="left:16px;width:115px;background:linear-gradient(160deg,#a47a52,#6e5644)" role="img" aria-label="Photo of an inspector checking roof shingles"></div>
  <div class="service" style="left:139px;width:116px;background:linear-gradient(160deg,#8a8a8a,#3d3d3d)" role="img" aria-label="Photo of a roofer repairing a gutter edge"></div>
  <div class="service" style="left:259px;width:116px;background:linear-gradient(160deg,#9cc3e6,#d7c5a6)" role="img" aria-label="Photo of roofers installing a new roof"></div>
  <div class="service__label" style="left:16px;width:115px">ROOF ANALYSIS</div>
  <div class="service__label" style="left:139px;width:116px">ROOF REPAIR</div>
  <div class="service__label" style="left:259px;width:116px">ROOF REPLACEMENT</div>

  <div class="badge" style="left:344px;top:273px">FINANCING<br>AVAILABLE</div>

  <div class="body-copy abs" style="left:16px;top:404px;font-size:12.5px;line-height:16px;text-align:left">ShingleGuide's Mission: to help you find cost-effective<br>and long-term solutions for prolonging the life of your roof.</div>

  <div class="return-address">SHINGLE GUIDE<br>1180 Maple Grove Rd.<br>Plymouth, MI 48170</div>
  <div class="stamp-box"></div>
  <div class="address-line" style="top:182px"></div>
  <div class="address-line" style="top:222px"></div>
  <div class="address-line" style="top:263px"></div>

  <div class="callbar"><span>SCHEDULE NOW!</span><span class="callbar__phone"><svg width="20" height="16" viewBox="0 0 20 16" aria-hidden="true"><path d="M1 6 Q10 -1 19 6 L16 8 L14 5 Q10 4 6 5 L4 8 Z" fill="#fff"/><path d="M5 8 L15 8 L18 15 L2 15 Z" fill="#fff"/><circle cx="10" cy="11" r="2" fill="var(--orange)"/></svg>(555) 014-ROOF</span></div>
  <div class="site">shingleguidemi-example.com</div>
</section>

</body>
</html>
```